Business Card Design

We are an IT staffing and consulting company providing IT solutions and resources to our clients.

Industry/Entity Type

Business

Contact Information for Business Card

Ravindra Kolluparthi
Vice President

BrimTrail Inc
48260 Hollyfern Market Court, suite 700
Larkmont, VA 20199
Direct: 571-555-0193
Mobile: 571-555-0147
Email: Ravindra@brimtrailinc.example
Fax: 703-555-0162
www.brimtrailinc.example

```html
<!DOCTYPE html>
<html lang="en">
<head>
<meta charset="utf-8">
<title>BrimTrail Inc – Business Card</title>
<link rel="stylesheet" href="https://fonts.googleapis.com/css2?family=Roboto+Condensed:wght@400;700&family=Tinos&display=swap">
<style>
  :root {
    --backdrop: #d9d6d0;
    --card-black: #050505;
    --band-yellow: #fff200;
    --name-red: #e0161c;
    --text-light: #e8e8e8;
    --text-soft: #c9c9c9;
    --rule-grey: #9a9a9a;
    --mark-ink: #1a1a1a;
  }
  * { margin: 0; padding: 0; box-sizing: border-box; }
  html, body {
    width: 1200px;
    height: 901px;
    overflow: hidden;
    background: var(--backdrop);
  }
  .canvas {
    position: relative;
    width: 1200px;
    height: 901px;
  }
  .business-card {
    position: absolute;
    left: 180px;
    top: 210px;
    width: 840px;
    height: 480px;
    background: var(--card-black);
    box-shadow: 0 14px 34px rgba(0,0,0,.35);
    overflow: hidden;
  }
  .brand-band {
    position: absolute;
    left: 0;
    top: 268px;
    width: 372px;
    height: 104px;
    background: var(--band-yellow);
    display: flex;
    align-items: center;
    justify-content: center;
  }
  .brand-name {
    font-family: "Roboto Condensed", sans-serif;
    font-weight: 400;
    font-size: 52px;
    letter-spacing: 1px;
    color: var(--mark-ink);
  }
  .divider-rule {
    position: absolute;
    left: 372px;
    top: 118px;
    width: 2px;
    height: 254px;
    background: var(--rule-grey);
  }
  .contact-block {
    position: absolute;
    left: 392px;
    top: 112px;
    font-family: "Tinos", serif;
    color: var(--text-light);
  }
  .person-name {
    font-family: "Roboto Condensed", sans-serif;
    font-weight: 700;
    font-size: 32px;
    color: var(--name-red);
    line-height: 1.1;
  }
  .person-title {
    font-size: 15px;
    color: var(--text-soft);
    margin-bottom: 22px;
  }
  .line { line-height: 1.35; }
  .line-phone { font-size: 19px; }
  .line-address { font-size: 13px; color: var(--text-soft); margin-bottom: 8px; }
  .line-email, .line-fax, .line-web { font-size: 21px; }
</style>
</head>
<body>
  <main class="canvas">
    <section class="business-card" aria-label="Business card front">
      <div class="brand-band">
        <span class="brand-name">BrimTrail</span>
      </div>
      <div class="divider-rule"></div>
      <div class="contact-block">
        <h1 class="person-name">Ravindra Kolluparthi</h1>
        <p class="person-title">Vice President BrimTrail Inc.</p>
        <p class="line line-phone">571-555-0193 | 571-555-0147</p>
        <p class="line line-address">48260 Hollyfern Market Court, suite 700 Larkmont, VA 20199.</p>
        <p class="line line-email">Ravindra@brimtrailinc.example</p>
        <p class="line line-fax">703-555-0162</p>
        <p class="line line-web">www.brimtrailinc.example</p>
      </div>
    </section>
  </main>
</body>
</html>
```